Korvex Systems*

Stationary design including business cards, letter heads, envelops and email signatures using our new logo

Target Market(s)

Innovative Technologies

Industry/Entity Type

Defense Contracting

Font styles to use
Sans Serif

```html
<!DOCTYPE html>
<html lang="en">
<head>
<meta charset="utf-8">
<title>Korvex Systems – Business Cards</title>
<link rel="stylesheet" href="https://fonts.googleapis.com/css2?family=Roboto:wght@300;400;500&display=swap">
<style>
  :root {
    --backdrop: #242424;
    --card: #2b2a28;
    --ink: #f2f2f0;
    --ink-soft: #cfcfcb;
    --shadow: rgba(0, 0, 0, 0.45);
  }
  * { margin: 0; padding: 0; box-sizing: border-box; }
  html, body {
    width: 1200px; height: 840px; overflow: hidden;
    background: var(--backdrop);
    font-family: "Roboto", sans-serif;
    color: var(--ink);
  }
  .stage {
    position: relative; width: 1200px; height: 840px;
    display: flex; justify-content: center; align-items: center; gap: 60px;
  }
  .card {
    position: relative; width: 300px; height: 525px;
    background: var(--card);
    box-shadow: 0 18px 40px var(--shadow);
  }

  /* Front */
  .card--front { display: flex; flex-direction: column; align-items: center; text-align: center; padding-top: 58px; }
  .holder-name { font-size: 19px; font-weight: 500; letter-spacing: 1.5px; text-transform: uppercase; }
  .holder-title { margin-top: 4px; font-size: 10px; font-weight: 300; letter-spacing: 1.6px; text-transform: uppercase; color: var(--ink-soft); }
  .brand-name {
    margin-top: 86px; font-size: 25px; font-weight: 500;
    letter-spacing: 1px; text-transform: uppercase; line-height: 1.1;
  }
  .contact-icons { margin-top: 34px; display: flex; gap: 12px; }
  .contact-icons svg { width: 16px; height: 16px; }
  .contact-list { margin-top: 14px; list-style: none; font-size: 12px; font-weight: 400; letter-spacing: 0.4px; line-height: 2; }
  .divider { margin-top: 16px; display: flex; align-items: center; gap: 10px; }
  .divider span { display: block; width: 16px; height: 1.5px; background: var(--ink); }
  .divider svg { width: 16px; height: 16px; }
  .address { margin-top: 12px; font-style: normal; font-size: 12px; letter-spacing: 0.4px; line-height: 1.45; }

  /* Back */
  .accent-rule { position: absolute; left: 44px; top: 42px; width: 1.5px; height: 36px; background: var(--ink); }
  .web-vertical {
    position: absolute; left: 38px; top: 100px;
    writing-mode: vertical-rl; font-size: 13px; letter-spacing: 1.2px;
  }
  .card--back .brand-name {
    position: absolute; right: 34px; bottom: 60px; margin: 0;
    font-size: 33px; text-align: right;
  }
</style>
</head>
<body>
<main class="stage">
  <section class="card card--front" aria-label="Business card front">
    <h1 class="holder-name">Daniel Verhoeven</h1>
    <p class="holder-title">Managing Director</p>

    <p class="brand-name">Korvex Systems</p>

    <div class="contact-icons" aria-hidden="true">
      <svg viewBox="0 0 16 16"><circle cx="8" cy="8" r="7.3" fill="none" stroke="#f2f2f0" stroke-width="0.8"/><path d="M5.6 4.6l1.2 1.5-.7.9c.5 1 1.3 1.8 2.3 2.3l.9-.7 1.5 1.2-.8 1.1c-2.5-.4-4.6-2.5-5-5z" fill="#f2f2f0"/></svg>
      <svg viewBox="0 0 16 16"><circle cx="8" cy="8" r="7.3" fill="none" stroke="#f2f2f0" stroke-width="0.8"/><circle cx="8" cy="8" r="3.6" fill="none" stroke="#f2f2f0" stroke-width="0.8"/><ellipse cx="8" cy="8" rx="1.5" ry="3.6" fill="none" stroke="#f2f2f0" stroke-width="0.7"/><line x1="4.4" y1="8" x2="11.6" y2="8" stroke="#f2f2f0" stroke-width="0.7"/></svg>
      <svg viewBox="0 0 16 16"><circle cx="8" cy="8" r="7.3" fill="none" stroke="#f2f2f0" stroke-width="0.8"/><rect x="4.3" y="5.3" width="7.4" height="5.4" fill="#f2f2f0"/><path d="M4.3 5.3L8 8.3l3.7-3" fill="none" stroke="#2b2a28" stroke-width="0.7"/></svg>
    </div>

    <ul class="contact-list">
      <li>555 010-2284</li>
      <li>contact@korvexsystems.com</li>
      <li>www.korvexsystems.com</li>
    </ul>

    <div class="divider" aria-hidden="true">
      <span></span>
      <svg viewBox="0 0 16 16"><circle cx="8" cy="8" r="7.3" fill="none" stroke="#f2f2f0" stroke-width="0.8"/><path d="M8 12s-3-3-3-5.2a3 3 0 016 0C11 9 8 12 8 12z" fill="none" stroke="#f2f2f0" stroke-width="0.8"/><circle cx="8" cy="6.8" r="1" fill="#f2f2f0"/></svg>
      <span></span>
    </div>

    <address class="address">
      418 Larchmont Ave<br>
      #B72 Harbor Point<br>
      CA 90017
    </address>
  </section>

  <section class="card card--back" aria-label="Business card back">
    <span class="accent-rule" aria-hidden="true"></span>
    <p class="web-vertical">www.korvexsystems.com</p>
    <p class="brand-name">Korvex Systems</p>
  </section>
</main>
</body>
</html>
```